Homepage Design :) --- A website that connects Journalists to Sources to make brilliant news stories

I need a new homepage designed for a company based in California. The homepage is simple.
The website is QuillBridgeConnect.com.

About us:
We are a platform that connects reporters to expert sources (normal people with specific expertise) so a reporter can quickly and easily source information for their news story. Also, the source gets cited in their major news article so it's a win-win situation.

Design:
We have no real slogan except maybe the slogan on the website (beautiful stories that connect us), though that can change too.

I would like to see designs of any style that you choose. We really only have one website color shown in blue on the website, you can use other colors in addition to that one or even change the theme color.

Attachments:
- Homepage to redesign, which you can go to the website yourself to check it out
- A mockup sketch of a revision idea that I had in mind with two people thinking short thoughts. Though this is just a random thought.... You can make anything you want! :)
- An image of what the logged in dashboard looks like just if you want a reference

The footer menu links will remain but can be anything color/style.

Make any ideas you want, keep the same amount of sections or add more, add any graphics or things that you want, etc. I want creativity to really attract customers the second they land on the page. A powerfully beautiful home page!

For reference, some competing websites are NewsDeskLink.com, Vornip.io, and plivex.com
I noticed all these website use red/orange related colors, so maybe I should change the color theme to that? Again, your decision :)

```html
<!DOCTYPE html>
<html lang="en">
<head>
<meta charset="utf-8">
<title>QuillBridge Connect — Home</title>
<link href="https://fonts.googleapis.com/css2?family=Roboto+Slab:wght@700&family=Roboto:wght@400;500;700&display=swap" rel="stylesheet">
<style>
:root{
  --red:#f4472b;
  --purple:#6a55e8;
  --ink:#262626;
  --text:#333;
  --muted:#555;
  --grey:#efefef;
  --white:#fff;
}
*{box-sizing:border-box;margin:0;padding:0}
html,body{width:1200px;height:2962px;overflow:hidden}
body{position:relative;background:var(--white);font-family:Roboto,Arial,sans-serif;color:var(--text)}
.abs{position:absolute}
.slab{font-family:"Roboto Slab",Georgia,serif;font-weight:700}
.btn{position:absolute;display:flex;align-items:center;justify-content:center;font:700 14px Roboto,sans-serif;text-transform:uppercase;border-radius:3px;box-shadow:0 4px 10px rgba(0,0,0,.15)}
.btn-outline{background:var(--white);border:2px solid var(--purple);color:var(--ink)}
.btn-solid{background:var(--red);color:var(--white)}
/* header */
.brand{left:110px;top:46px;font-size:34px;color:var(--ink);line-height:1.1}
.nav{left:384px;top:62px;display:flex;gap:32px;font:500 14px Roboto,sans-serif;color:var(--ink)}
.nav .active{color:var(--red)}
/* hero */
.hero-photo{left:0;top:137px;width:1200px;height:668px;background:linear-gradient(100deg,#7d7e74 0%,#bdb8ae 35%,#e9e7df 65%,#f6f5ef 100%);clip-path:polygon(0 0,100% 0,100% 503px,0 668px)}
.bubble-icon{border-radius:50%;background:var(--white);box-shadow:0 4px 14px rgba(0,0,0,.2);display:flex;align-items:center;justify-content:center}
.bubble-text{background:var(--white);font-size:14px;line-height:24px;color:var(--ink);padding:0 22px;display:flex;align-items:center}
.hero-title{left:664px;top:298px;font-size:39px;line-height:48px;color:var(--ink)}
.hero-sub{left:664px;top:410px;font-size:23px;color:#444}
/* sections */
.section-title{left:0;width:1200px;text-align:center;color:var(--ink)}
.underline{height:4px;background:var(--red)}
.card{background:var(--white);box-shadow:0 4px 18px rgba(0,0,0,.12);border-radius:4px;width:305px;height:273px;top:972px;text-align:center}
.card .icon{width:88px;height:88px;border-radius:50%;margin:42px auto 0;display:flex;align-items:center;justify-content:center}
.card p{margin-top:28px;padding:0 40px;font:700 16px/27px Roboto,sans-serif;text-transform:uppercase;color:var(--ink)}
.lead{left:0;width:1200px;text-align:center;top:1648px;font-size:22px;color:#444}
/* start */
.start-photo{left:117px;top:1986px;width:549px;height:424px;background:linear-gradient(135deg,#6f6a4f,#b59a7a 45%,#2f3656 80%);outline:4px solid var(--white);box-shadow:0 4px 18px rgba(0,0,0,.15)}
.start-card{left:528px;top:2108px;width:560px;height:382px;background:var(--white);box-shadow:0 4px 22px rgba(0,0,0,.12);padding:58px 54px 0}
.start-card h2{font-size:31px;color:var(--ink)}
.start-card p{margin-top:44px;font-size:16px;line-height:28.5px;color:var(--muted);text-align:justify}
/* footer */
.foot-brand{left:110px;top:2786px;font-size:30px;color:var(--white)}
.foot-col{top:2755px;color:var(--white)}
.foot-col h4{font:700 17px Roboto,sans-serif;text-transform:uppercase;margin-bottom:14px}
.foot-col li{list-style:none;font-size:15px;height:31px;display:flex;align-items:center;gap:24px}
.foot-col li::before{content:"";width:13px;height:13px;border-radius:50%;background:var(--red);flex:none}
.divider{left:110px;top:2900px;width:978px;height:1px;background:#555}
.copy{left:0;width:1200px;top:2918px;text-align:center;color:var(--white);font-size:12.5px}
</style>
</head>
<body>

<!-- Header -->
<div class="abs brand slab">QuillBridge</div>
<nav class="abs nav"><span class="active">HOME</span><span>HOW IT WORKS</span><span>JOB BOARD</span><span>CONTACT US</span></nav>
<div class="btn btn-outline" style="left:839px;top:48px;width:118px;height:45px">&#9679;&nbsp; Sign up</div>
<div class="btn btn-solid" style="left:969px;top:48px;width:119px;height:45px">&#9679;&nbsp; Log in</div>

<!-- Hero -->
<div class="abs hero-photo" role="img" aria-label="Photo of a reporter holding a microphone interviewing a man on a sofa in a bright room"></div>
<svg class="abs" style="left:0;top:0" width="1200" height="830"><polygon points="870,717 1200,672 1200,803" fill="#6a55e8"/></svg>

<div class="abs bubble-icon" style="left:55px;top:188px;width:84px;height:84px">
  <div style="width:70px;height:70px;border-radius:50%;background:var(--red);display:flex;align-items:center;justify-content:center">
    <svg width="36" height="36" viewBox="0 0 36 36" fill="none" stroke="#fff" stroke-width="2"><circle cx="18" cy="18" r="11"/><circle cx="18" cy="18" r="4"/><path d="M18 3v4M18 29v4M3 18h4M29 18h4"/></svg>
  </div>
</div>
<div class="abs bubble-text" style="left:166px;top:192px;width:283px;height:79px">I'm an Expert Source. I can simply provide my knowledge and get Cited.</div>

<div class="abs bubble-text" style="left:347px;top:566px;width:136px;height:46px">I'm a Reporter</div>
<div class="abs bubble-icon" style="left:519px;top:550px;width:76px;height:76px">
  <svg width="38" height="38" viewBox="0 0 38 38" fill="none" stroke="#6a55e8" stroke-width="1.8"><circle cx="15" cy="14" r="6"/><path d="M5 34c0-7 4-11 10-11s10 4 10 11"/><rect x="23" y="4" width="12" height="9" rx="1"/></svg>
</div>

<h1 class="abs hero-title slab">EXPERIENCE<br>INSPIRING REPORTING</h1>
<div class="abs hero-sub">Beautiful Stories That Connect Us</div>
<div class="btn btn-outline" style="left:665px;top:469px;width:118px;height:45px">Reporters</div>
<div class="btn btn-solid" style="left:795px;top:469px;width:119px;height:45px">Sources</div>

<!-- What we do -->
<h2 class="abs section-title slab" style="top:855px;font-size:46px">WHAT WE DO</h2>
<div class="abs underline" style="left:553px;top:914px;width:93px"></div>

<div class="abs card" style="left:111px">
  <div class="icon" style="background:var(--purple)"><svg width="48" height="48" viewBox="0 0 48 48" fill="none" stroke="#fff" stroke-width="2"><circle cx="20" cy="20" r="14"/><path d="M6 20h28M20 6c-6 8-6 20 0 28M20 6c6 8 6 20 0 28"/><circle cx="32" cy="32" r="6"/><path d="M36 36l7 7"/></svg></div>
  <p>Find sources for the stories that you need information.</p>
</div>
<div class="abs card" style="left:447px">
  <div class="icon" style="background:var(--red)"><svg width="48" height="48" viewBox="0 0 48 48" fill="none" stroke="#fff" stroke-width="2"><rect x="8" y="8" width="32" height="30" rx="2"/><path d="M8 14h32M28 20h8M28 26h8"/><circle cx="19" cy="27" r="6"/><path d="M23 31l6 8"/></svg></div>
  <p>Browse profiles of your sources to verify expertise.</p>
</div>
<div class="abs card" style="left:783px">
  <div class="icon" style="background:var(--purple)"><svg width="48" height="48" viewBox="0 0 48 48" fill="none" stroke="#fff" stroke-width="2"><path d="M18 38h10M19 42h8M23 34c0-4-8-6-8-14a9 9 0 0 1 18 0c0 8-8 10-8 14"/><circle cx="31" cy="17" r="5"/><path d="M8 10l4 3M40 10l-4 3M24 3v4"/></svg></div>
  <p>Explore pitches to discover new topics.</p>
</div>

<!-- Our reporters -->
<svg class="abs" style="left:0;top:1340px" width="1200" height="520">
  <polygon points="0,180 1200,15 1200,515 0,515" fill="#efefef"/>
  <polygon points="0,17 330,102 0,150" fill="#f4472b"/>
</svg>
<h2 class="abs section-title slab" style="top:1550px;font-size:46px">OUR REPORTERS</h2>
<div class="abs underline" style="left:553px;top:1612px;width:93px"></div>
<div class="abs lead">Thousands of Reporters &amp; Journalists Millions of sources One Great Story.</div>
<div class="btn btn-outline" style="left:415px;top:1713px;width:179px;height:45px">Reporters sign up</div>
<div class="btn btn-solid" style="left:605px;top:1713px;width:180px;height:45px">Sources sign up</div>

<!-- Get ready -->
<svg class="abs" style="left:0;top:2070px" width="1200" height="380" fill="none" stroke="#6a55e8" stroke-width="3">
  <path d="M672 7H1055V40"/>
  <path d="M499 340V367H530"/>
</svg>
<div class="abs start-photo" role="img" aria-label="Photo of a smiling young woman with glasses sitting at a desk"></div>
<div class="abs start-card">
  <h2 class="slab">GET READY TO START?</h2>
  <div class="underline" style="width:93px;margin-top:6px"></div>
  <p>QuillBridge Connect (QBC) connects reporters and sources from around the world. You want the real, honest stories. We connect you to the experts.</p>
</div>
<div class="btn btn-solid" style="left:582px;top:2372px;width:142px;height:45px">Get started</div>

<!-- Footer -->
<svg class="abs" style="left:0;top:2550px" width="1200" height="412">
  <polygon points="0,12 1200,175 1200,412 0,412" fill="#262626"/>
  <polygon points="870,122 1200,15 1200,145" fill="#6a55e8"/>
</svg>
<div class="abs foot-brand slab">QuillBridge</div>
<div class="abs foot-col" style="left:382px"><h4>About</h4><ul><li>Contact us</li><li>How it works</li><li>Job Board</li></ul></div>
<div class="abs foot-col" style="left:622px"><h4>Information</h4><ul><li>Terms of Service</li><li>Privacy Policy</li></ul></div>
<div class="abs foot-col" style="left:894px"><h4>Rules</h4><ul><li>Reporter &amp; Source Rules</li><li>Refund Policy</li></ul></div>
<div class="abs divider"></div>
<div class="abs copy">© 2023 <b style="font-weight:500">QUILLBRIDGE CONNECT</b> &nbsp;|&nbsp; All Rights Reserved</div>

</body>
</html>
```